Design Shopify E-Commerce Website for Men's Products

Design a Shopify website for men to sell our men's jewelry, cigar and bar accessories, and other men's products. Design should be hip, with like a rock n' roll, biker, whiskey driker flare. Name of the company is "Outlaw Cupboard" and website will be www.OutlawCupboard.com
Homepage will have navigation bar with three categories: Men's Jewelry, Cigar & Bar Products, Man Cave Swag
I will upload our logo, inspiration type pictures and some of the products that we sell
Theme colors should be mainly dark: black, grey, brown, gold

```html
<!DOCTYPE html>
<html lang="en">
<head>
<meta charset="utf-8">
<title>Outlaw Cupboard</title>
<link rel="stylesheet" href="https://fonts.googleapis.com/css2?family=Oswald:wght@300;400;500&family=Poppins:ital,wght@0,400;0,500;0,600;1,400&display=swap">
<style>
:root{
  --black:#050505;
  --coal:#141414;
  --grey:#1f1e1d;
  --gold:#c9a24a;
  --gold-light:#e6c57a;
  --gold-deep:#a57e2e;
  --amber:#8a4a14;
  --text:#e9e4d8;
  --muted:#b8b2a6;
}
*{box-sizing:border-box;margin:0;padding:0}
html,body{width:1200px;height:4351px;overflow:hidden;background:var(--black);color:var(--text);font-family:"Poppins",sans-serif}
.page{position:relative;width:1200px;height:4351px}
.abs{position:absolute}
.heading{font-family:"Oswald",sans-serif;font-weight:300;color:var(--gold);text-transform:uppercase;letter-spacing:.5px}
.btn{position:absolute;display:flex;align-items:center;justify-content:center;background:linear-gradient(90deg,var(--gold-light),var(--gold-deep));color:#1a1206;font-weight:600;font-size:14px;text-transform:uppercase;clip-path:polygon(0 0,100% 0,100% 70%,92% 100%,0 100%)}
.brand{font-family:"Oswald",sans-serif;font-weight:400;color:var(--gold);text-transform:uppercase;display:flex;align-items:center;gap:8px;text-align:center;line-height:1.05}
.brand-dot{width:14px;height:14px;border-radius:50%;background:var(--gold);flex:none}

/* hero */
.hero{position:absolute;left:0;top:0;width:1200px;height:703px;background:radial-gradient(ellipse at 78% 45%,#9a5516 0%,#4a2410 28%,transparent 55%),radial-gradient(ellipse at 50% 65%,#3a2a20 0%,transparent 40%),linear-gradient(180deg,#1a120d 0%,#2a1a10 60%,#3a2a20 100%)}
.nav-link{position:absolute;top:42px;font-size:15px;color:#fff}
.nav-icon{position:absolute;top:44px}
.hero-title{left:127px;top:262px;font-size:58px;line-height:54px;font-weight:400}
.hero-text{left:127px;top:395px;width:340px;font-size:15.5px;line-height:22px;color:#fff}

/* categories */
.cat{position:absolute;top:781px;width:302px;height:334px;display:flex;align-items:flex-end;justify-content:center;padding-bottom:32px}
.cat span{font-family:"Oswald",sans-serif;font-size:21px;color:#fff;text-transform:uppercase}
.cat-1{left:122px;background:linear-gradient(180deg,#8a8478 0%,#6e6558 50%,#c9a24a 100%)}
.cat-2{left:445px;background:linear-gradient(180deg,#5a2a14 0%,#7a3a1a 45%,#c9a24a 100%)}
.cat-3{left:769px;background:linear-gradient(180deg,#c9b79a 0%,#9a7e5c 50%,#c9a24a 100%)}

/* about */
.about-mark{left:169px;top:1251px;width:397px;height:380px;display:flex;align-items:center;justify-content:center}
.about-title{left:636px;top:1272px;font-size:46px;line-height:52px}
.about-text{left:644px;top:1384px;width:430px;font-size:15.5px;line-height:22.4px}

/* products */
.products{position:absolute;left:0;top:1766px;width:1200px;height:578px;background:linear-gradient(180deg,#1d1c1b,#151414)}
.section-title{position:absolute;left:0;width:1200px;text-align:center;font-size:45px}
.card{position:absolute;top:181px;width:222px;height:271px;border:1px solid var(--gold-deep);text-align:center}
.card .thumb{position:absolute;left:31px;top:25px;width:160px;height:130px;border-radius:4px}
.card .name{position:absolute;left:0;right:0;top:170px;font-size:17px;color:#fff;text-transform:uppercase}
.card .price{position:absolute;left:0;right:0;top:200px;font-size:16px;font-weight:600;color:var(--gold)}
.arrow{position:absolute}

/* testimonial */
.quote-box{left:208px;top:2552px;width:792px;height:301px;border:1.5px solid var(--gold-deep)}
.avatar{left:545px;top:2484px;width:118px;height:118px;border-radius:50%;border:2px solid var(--gold);background:radial-gradient(circle at 50% 40%,#4a5a6a,#1a2230)}
.quote-name{left:0;width:1200px;top:2633px;text-align:center;font-size:18px;font-weight:600;color:var(--gold)}
.quote-text{left:260px;width:690px;top:2683px;text-align:center;font-size:16px;font-style:italic;line-height:22.5px}

/* gallery */
.gallery-text{left:200px;width:800px;top:3025px;text-align:center;font-size:15.5px;line-height:21px}
.shot{position:absolute;top:3108px;width:233px;height:304px}
.mood{position:absolute;left:0;top:3160px;width:1200px;height:744px;background:radial-gradient(ellipse at 83% 55%,#7a3c10 0%,#3a1c08 25%,transparent 50%),radial-gradient(ellipse at 45% 85%,#2e241c 0%,transparent 45%),linear-gradient(180deg,#050505 0%,#16100b 35%,#1d140e 100%)}
.connect-text{left:280px;width:640px;top:3665px;text-align:center;font-size:15.5px;line-height:21px}
.email{left:343px;top:3737px;width:514px;height:49px;border:1.5px solid #d8d3c8;background:#0e0c0a;font-size:14px;color:#fff;padding:0 12px;display:flex;align-items:center}

/* footer */
.footer{position:absolute;left:0;top:3904px;width:1200px;height:447px;background:var(--coal)}
.foot-title{font-size:28px}
.foot-line{position:absolute;font-size:15px;color:var(--text);display:flex;align-items:center;gap:9px}
.rule{left:127px;top:4223px;width:944px;height:1px;background:#3a3834}
.card-badge{position:absolute;top:4260px;width:37px;height:22px;border-radius:3px}
.copy{left:0;width:1200px;top:4306px;text-align:center;font-size:14px;color:var(--muted)}
</style>
</head>
<body>
<div class="page">

  <!-- hero -->
  <section class="hero" role="img" aria-label="Glass of whiskey on ice beside a cigar in a glass ashtray, warm bar lights behind"></section>
  <div class="brand abs" style="left:110px;top:50px;width:150px;font-size:22px"><span class="brand-dot"></span>Outlaw Cupboard</div>
  <a class="nav-link" style="left:362px">Men's Jewelry</a>
  <a class="nav-link" style="left:510px">Cigar &amp; Bar Products</a>
  <a class="nav-link" style="left:711px">Man Cave Swag</a>
  <svg class="nav-icon" style="left:984px" width="16" height="16" viewBox="0 0 16 16" fill="none" stroke="#c9a24a" stroke-width="2.2"><circle cx="6.5" cy="6.5" r="4.5"/><path d="M10 10l4.5 4.5"/></svg>
  <svg class="nav-icon" style="left:1016px" width="16" height="16" viewBox="0 0 16 16" fill="#c9a24a"><path d="M2 5h12l-1 10H3z"/><path d="M5 5V3.5a3 3 0 016 0V5" fill="none" stroke="#c9a24a" stroke-width="1.6"/></svg>
  <svg class="nav-icon" style="left:1048px" width="16" height="16" viewBox="0 0 16 16" fill="#c9a24a"><circle cx="8" cy="4.5" r="3.5"/><path d="M1.5 16a6.5 6.5 0 0113 0z"/></svg>
  <h1 class="heading abs hero-title">Outlaw<br>Cupboard</h1>
  <p class="abs hero-text">Lorem ipsum dolor sit amet, consectetur adipiscing elit, sed do eiusmod tempor inc didunt ut labore et dolore magna.</p>
  <a class="btn" style="left:127px;top:487px;width:142px;height:39px">Shop Now</a>

  <!-- categories -->
  <a class="cat cat-1" role="img" aria-label="Pair of silver cufflinks on weathered wood"><span>Men's Jewelry</span></a>
  <a class="cat cat-2" role="img" aria-label="Open box of cigars"><span>Cigar and Bar Accessories</span></a>
  <a class="cat cat-3" role="img" aria-label="Shaving brush and razor on a stand"><span>Other Men's Products</span></a>

  <!-- about -->
  <div class="abs about-mark"><div class="brand" style="font-size:48px;width:330px;justify-content:center"><span class="brand-dot" style="width:26px;height:26px"></span>Outlaw Cupboard</div></div>
  <h2 class="heading abs about-title">About<br>Outlaw Cupboard</h2>
  <p class="abs about-text">Sed ut perspiciatis unde omnis iste natuserror sit volup tatem accusantium doloremque lud antium, totam rem aperiam, eaque ipsa quae ab illo inventore verita tis et quasi architecto beatae vitae dicta sunt expli cabo. Nemo enim ipsam voluptatem quia voluptas sit asperatur aut odit aut fugit, sed quia consequuntur ma gni dolores eos qui ratione voluptatem squi nesciunt. Neque porro quisquam est.</p>
  <a class="btn" style="left:644px;top:1585px;width:139px;height:35px">Read More</a>

  <!-- products -->
  <section class="products">
    <h2 class="heading section-title" style="top:98px">Our Products</h2>
    <svg class="arrow" style="left:74px;top:274px" width="10" height="16" viewBox="0 0 10 16" fill="none" stroke="#c9a24a" stroke-width="2"><path d="M8 2L2 8l6 6"/></svg>
    <svg class="arrow" style="left:1110px;top:274px" width="10" height="16" viewBox="0 0 10 16" fill="none" stroke="#c9a24a" stroke-width="2"><path d="M2 2l6 6-6 6"/></svg>
    <div class="card" style="left:122px"><div class="thumb" role="img" aria-label="Red lacquered cigar humidor" style="background:linear-gradient(160deg,#9a2a2a,#5a1414)"></div><div class="name">Cigar Humidor</div><div class="price">$29.00 USD</div></div>
    <div class="card" style="left:367px"><div class="thumb" role="img" aria-label="Wooden whiskey set case" style="background:linear-gradient(160deg,#5a3a2a,#2a1a14)"></div><div class="name">Whiskeyset</div><div class="price">$29.00 USD</div></div>
    <div class="card" style="left:612px"><div class="thumb" role="img" aria-label="Octagonal cigar ashtray" style="background:linear-gradient(160deg,#7a2a2a,#3a1414)"></div><div class="name">Cigarashtray</div><div class="price">$29.00 USD</div></div>
    <div class="card" style="left:857px"><div class="thumb" role="img" aria-label="Heavy silver and gold ring" style="background:linear-gradient(160deg,#8a8680,#3a3630)"></div><div class="name">Heavyring</div><div class="price">$29.00 USD</div></div>
  </section>

  <!-- testimonials -->
  <h2 class="heading section-title" style="top:2428px">Client Testimonials</h2>
  <div class="abs quote-box"></div>
  <div class="abs avatar" role="img" aria-label="Portrait of the client"></div>
  <div class="abs quote-name">MARCUS T</div>
  <p class="abs quote-text">Lorem ipsum dolor sit ameconsectetur adipiscing elitse do eiusmod tempor idnt ut labore et dolore mag na aliquaLorem ipsum dolor sit ameconsectetur adipiscing elitse do eiusmod tempor incid idnt ut labore et dolore mag na aliqua. Quis ipsum suspen disse ultrices gravida. is ipsum suspen ds gravida.</p>
  <svg class="abs" style="left:538px;top:2795px" width="124" height="24" viewBox="0 0 124 24" fill="#f5c518">
    <path id="st" d="M12 1l3.2 7 7.6.7-5.8 5 1.8 7.5L12 17.3 5.2 21.2 7 13.7 1.2 8.7l7.6-.7z"/>
    <use href="#st" x="25"/><use href="#st" x="50"/><use href="#st" x="75"/><use href="#st" x="100"/>
  </svg>
  <svg class="arrow" style="left:150px;top:2698px" width="10" height="16" viewBox="0 0 10 16" fill="none" stroke="#d8d3c8" stroke-width="2"><path d="M8 2L2 8l6 6"/></svg>
  <svg class="arrow" style="left:1037px;top:2698px" width="10" height="16" viewBox="0 0 10 16" fill="none" stroke="#d8d3c8" stroke-width="2"><path d="M2 2l6 6-6 6"/></svg>

  <!-- gallery & connect -->
  <div class="mood" role="img" aria-label="Faded backdrop of whiskey glass and cigar in warm bar light"></div>
  <h2 class="heading section-title" style="top:2955px">Our Gallery</h2>
  <p class="abs gallery-text">Lorem ipsum dolor sit amet, consectetur adipiscing elit, sed do eiusmod tempor incididunt ut labore et dolore magna aliquauis ipsum suspendisse ultrices gravida. Risus commodo viverra maecenas.</p>
  <div class="shot" style="left:108px;background:linear-gradient(150deg,#d8d8d8,#444 55%,#111)" role="img" aria-label="Chrome motorcycle exhaust close-up"></div>
  <div class="shot" style="left:358px;background:linear-gradient(160deg,#e8e4dc 0%,#8a4a22 40%,#4a2410 100%)" role="img" aria-label="Wooden desktop cigar cutter"></div>
  <div class="shot" style="left:610px;background:linear-gradient(150deg,#2a2a2a,#4a4a4a 50%,#1a1a1a)" role="img" aria-label="Pearl and chain necklace on leather"></div>
  <div class="shot" style="left:860px;background:linear-gradient(160deg,#8a7a66,#5a4a3a 50%,#3a2e22)" role="img" aria-label="Silver cufflinks on wood"></div>
  <a class="btn" style="left:529px;top:3466px;width:142px;height:39px">Follow Us</a>

  <h2 class="heading section-title" style="top:3595px">Let's Stay Connected</h2>
  <p class="abs connect-text">Lorem ipsum dolor sit amet, consectetur adipiscing elit, sed do eiusmod tempor incididunt ut labore et dolore magna aliquauis ipsum suspendisse ultric.</p>
  <div class="abs email">EMAIL:</div>
  <a class="btn" style="left:733px;top:3741px;width:117px;height:41px">Sign Up</a>

  <!-- footer -->
  <footer class="footer"></footer>
  <h3 class="heading abs foot-title" style="left:216px;top:3985px">Contact Us</h3>
  <div class="foot-line" style="left:216px;top:4034px"><svg width="14" height="14" viewBox="0 0 16 16" fill="#e9e4d8"><path d="M3 1l3 .5 1 3.5-2 1.5a9 9 0 005 5l1.5-2 3.5 1 .5 3-2 2C7 15 1 9 1 3z"/></svg>Ph: 55 01 2468</div>
  <div class="foot-line" style="left:216px;top:4064px"><svg width="14" height="12" viewBox="0 0 16 12" fill="#e9e4d8"><path d="M0 0h16v12H0z"/><path d="M0 0l8 6 8-6" fill="none" stroke="#141414" stroke-width="1.5"/></svg>info@OutlawCupboard.com</div>
  <div class="foot-line" style="left:216px;top:4095px"><svg width="12" height="16" viewBox="0 0 12 16" fill="#e9e4d8"><path d="M6 0a6 6 0 016 6c0 4-6 10-6 10S0 10 0 6a6 6 0 016-6z"/><circle cx="6" cy="6" r="2.2" fill="#141414"/></svg>Location Sample 10245</div>

  <div class="brand abs" style="left:510px;top:4062px;width:180px;font-size:24px;justify-content:center"><span class="brand-dot"></span>Outlaw Cupboard</div>

  <h3 class="heading abs foot-title" style="left:825px;top:3985px">Links</h3>
  <a class="foot-line" style="left:827px;top:4034px">Men's Jewelry</a>
  <a class="foot-line" style="left:827px;top:4064px">Cigar &amp; Bar Products</a>
  <a class="foot-line" style="left:827px;top:4095px">Man Cave Swag</a>

  <span class="abs" style="left:538px;top:4174px;width:20px;height:20px;border-radius:3px;background:#e9e4d8" aria-label="Social link"></span>
  <span class="abs" style="left:588px;top:4174px;width:20px;height:20px;border-radius:50%;border:2px solid #e9e4d8" aria-label="Social link"></span>
  <span class="abs" style="left:639px;top:4174px;width:20px;height:20px;border-radius:50%;background:#e9e4d8" aria-label="Social link"></span>

  <div class="abs rule"></div>
  <span class="card-badge" style="left:461px;background:#f2f2f2"></span>
  <span class="card-badge" style="left:508px;background:#f2f2f2"></span>
  <span class="card-badge" style="left:555px;background:#2a6ad8"></span>
  <span class="card-badge" style="left:602px;background:#f2f2f2"></span>
  <span class="card-badge" style="left:649px;background:#f2f2f2"></span>
  <span class="card-badge" style="left:696px;background:#f2f2f2"></span>
  <p class="abs copy">© 2023 Outlaw Cupboard. All rights are reserved.</p>

</div>
</body>
</html>
```